Design the Business card for VaultPeak

Business card required for a professional Cyber Security business.
Company Logo and Icon has already been provided however I would like other options for the logo and icon to compare to. Alternatively, please refine/enhance the image of the logo.icon I have already provided.

If you are going to use the provided logo and icon, I was thinking that the company raised Logo on White background would serve well on the front of the card. See attached. AND, a large company raised stand-alone icon to appear on black background on the back of the card with tagline 'Cyber Risk Management, Governance and Consulting' or 'Cyber Security for your Business' See attached.
Alternatively, provide your own design for the logo and icon.

Target Market(s)

Enterprise, Government, Financial.

Contact Information for Business Card

Teodor Halvik
Founder and CEO

Email Address
Mobile Number
Website URL
LinkedIn URL

Logo Text

VaultPeak - see attached example of logo

Font styles to use
Other font styles liked:
• Berlin Sans FB

Requirements
Must have
• Clean large and bold icon on the back with tagline.
• Horizontal alignment,
Nice to have
• Round edges.
• Raised Logo/Icon
Should not have
• An unprofessional look and feel.

```html
<!DOCTYPE html>
<html lang="en">
<head>
<meta charset="utf-8">
<title>VaultPeak Business Card</title>
<link rel="stylesheet" href="https://fonts.googleapis.com/css2?family=Roboto:wght@400&family=Roboto+Condensed:wght@500;700&family=Fredoka:wght@500&display=swap">
<style>
  :root {
    --backdrop: #262728;
    --card-light: #f4f4f4;
    --card-dark: #1b1d20;
    --brand-blue: #1a6fc0;
    --icon-blue: #4a6fc4;
    --accent-yellow: #f5b800;
    --text-grey: #444648;
    --rule-grey: #b9bcc2;
  }
  html, body {
    margin: 0;
    padding: 0;
    width: 1200px;
    height: 960px;
    overflow: hidden;
    background: var(--backdrop);
  }
  .canvas {
    position: relative;
    width: 1200px;
    height: 960px;
  }
  .card {
    position: absolute;
    border-radius: 18px;
    box-shadow: 0 3px 8px rgba(0,0,0,0.45);
    overflow: hidden;
  }
  .card-front {
    left: 322px; top: 108px; width: 599px; height: 342px;
    background: var(--card-light);
  }
  .card-back {
    left: 321px; top: 494px; width: 598px; height: 341px;
    background: var(--card-dark);
  }
  .timeline-rule {
    position: absolute;
    left: 33px; top: 0; width: 2px; height: 100%;
    background: var(--rule-grey);
  }
  .brand-lockup {
    position: absolute;
    right: 32px; top: 44px;
    display: flex; align-items: center; gap: 10px;
    font-family: "Fredoka", sans-serif;
    font-weight: 500;
    font-size: 33px;
    color: var(--brand-blue);
  }
  .brand-dot {
    width: 46px; height: 46px; border-radius: 50%;
    background: var(--icon-blue);
  }
  .row-icon {
    position: absolute;
    left: 24px;
    width: 22px; height: 22px;
  }
  .person-name {
    position: absolute; left: 62px; top: 128px; margin: 0;
    font-family: "Roboto Condensed", sans-serif;
    font-weight: 700; font-size: 24px;
    color: var(--brand-blue);
    letter-spacing: 0.2px;
  }
  .person-title {
    position: absolute; left: 62px; top: 155px; margin: 0;
    font-family: "Roboto Condensed", sans-serif;
    font-weight: 500; font-size: 15px;
    color: var(--accent-yellow);
  }
  .contact-line {
    position: absolute; left: 62px; margin: 0;
    font-family: "Roboto", sans-serif;
    font-size: 14.5px;
    color: var(--text-grey);
  }
  .back-lockup {
    position: absolute;
    left: 0; right: 0; top: 118px;
    display: flex; align-items: center; justify-content: center; gap: 16px;
    font-family: "Fredoka", sans-serif;
    font-weight: 500; font-size: 52px;
    color: var(--icon-blue);
  }
  .back-lockup .brand-dot { width: 72px; height: 72px; }
  .tagline {
    position: absolute; left: 0; right: 0; top: 274px; margin: 0;
    text-align: center;
    font-family: "Fredoka", sans-serif;
    font-weight: 500; font-size: 18px;
    color: var(--icon-blue);
  }
  .tagline .accent { color: var(--accent-yellow); }
</style>
</head>
<body>
<main class="canvas">

  <section class="card card-front" aria-label="Card front">
    <div class="timeline-rule"></div>

    <div class="brand-lockup">
      <span class="brand-dot"></span>
      <span>VaultPeak</span>
    </div>

    <svg class="row-icon" style="top:133px" viewBox="0 0 22 22" aria-hidden="true">
      <circle cx="11" cy="11" r="11" fill="var(--icon-blue)"/>
      <circle cx="11" cy="8.5" r="3.2" fill="#fff"/>
      <path d="M5.5 16.5c0-3 2.5-4.6 5.5-4.6s5.5 1.6 5.5 4.6z" fill="#fff"/>
    </svg>
    <h1 class="person-name">TEODOR HALVIK</h1>
    <p class="person-title">FOUNDER &amp; CEO</p>

    <svg class="row-icon" style="top:193px" viewBox="0 0 22 22" aria-hidden="true">
      <circle cx="11" cy="11" r="11" fill="var(--icon-blue)"/>
      <rect x="7.5" y="5" width="7" height="12" rx="1.2" fill="#fff"/>
      <rect x="8.7" y="6.5" width="4.6" height="8" fill="var(--icon-blue)"/>
    </svg>
    <p class="contact-line" style="top:194px">555 014 2290</p>

    <svg class="row-icon" style="top:229px" viewBox="0 0 22 22" aria-hidden="true">
      <circle cx="11" cy="11" r="11" fill="var(--icon-blue)"/>
      <rect x="5.5" y="7.5" width="11" height="7.5" fill="#fff"/>
      <path d="M5.5 7.5l5.5 4.2 5.5-4.2" fill="none" stroke="var(--icon-blue)" stroke-width="1"/>
    </svg>
    <p class="contact-line" style="top:230px">teodor@vaultpeak.com</p>

    <svg class="row-icon" style="top:264px" viewBox="0 0 22 22" aria-hidden="true">
      <circle cx="11" cy="11" r="11" fill="var(--icon-blue)"/>
      <circle cx="11" cy="11" r="5.5" fill="none" stroke="#fff" stroke-width="1.4"/>
      <path d="M5.5 11h11M11 5.5c-2.5 3-2.5 8 0 11M11 5.5c2.5 3 2.5 8 0 11" fill="none" stroke="#fff" stroke-width="1"/>
    </svg>
    <p class="contact-line" style="top:266px">www.vaultpeak.com</p>

    <svg class="row-icon" style="top:299px" viewBox="0 0 22 22" aria-hidden="true">
      <circle cx="11" cy="11" r="11" fill="var(--icon-blue)"/>
      <circle cx="11" cy="11" r="5" fill="#fff"/>
    </svg>
    <p class="contact-line" style="top:302px">vaultpeak</p>
  </section>

  <section class="card card-back" aria-label="Card back">
    <div class="back-lockup">
      <span class="brand-dot"></span>
      <span>VaultPeak</span>
    </div>
    <p class="tagline">Cyber Risk Management, <span class="accent">Governance &amp; Consulting</span></p>
  </section>

</main>
</body>
</html>
```